Business card Zottelgarten

Business card is for a self-employed dog trainer with own dog school. Name and logo of the dog school are available. Color specifications as well. The design should be classy and minimalist, but also modern. An already existing idea would be: Front: Only the logo Back: Contact data

Font styles to use
Serif
Sans Serif
Other font styles liked:
• Trajan Pro

Colors
f78f20

Requirements
Must have
• Name: Margit Wendler-Rasch Title: Dipl. Dog Trainer Contain my logo Follow my font and color preferences (see files)

```html
<!DOCTYPE html>
<html lang="en">
<head>
<meta charset="utf-8">
<title>Zottelgarten – Business Card Front and Back</title>
<link rel="stylesheet" href="https://fonts.googleapis.com/css2?family=Arimo:wght@400;700&family=Cinzel:wght@400;600&display=swap">
<style>
  :root {
    --backdrop: #ece8e3;
    --card-orange: #f78f20;
    --card-ink: #ffffff;
    --card-shadow: rgba(60, 40, 20, 0.22);
  }
  * { margin: 0; padding: 0; box-sizing: border-box; }
  html, body {
    width: 1200px;
    height: 756px;
    overflow: hidden;
    background: var(--backdrop);
    font-family: "Arimo", Arial, sans-serif;
  }
  .canvas {
    position: relative;
    width: 1200px;
    height: 756px;
  }
  .card {
    position: absolute;
    top: 228px;
    width: 540px;
    height: 300px;
    background: var(--card-orange);
    color: var(--card-ink);
    box-shadow: 0 8px 22px var(--card-shadow);
    overflow: hidden;
  }
  .card--front { left: 40px; }
  .card--back { left: 620px; }

  /* Front: double inset frame with centred school name box */
  .frame-outer {
    position: absolute;
    inset: 16px;
    border: 1.5px solid var(--card-ink);
  }
  .frame-inner {
    position: absolute;
    inset: 21px;
    border: 1.5px solid var(--card-ink);
  }
  .school-box {
    position: absolute;
    display: flex;
    align-items: center;
    justify-content: center;
    text-align: center;
    border: 1.5px solid var(--card-ink);
    font-family: "Cinzel", "Trajan Pro", Georgia, serif;
    font-weight: 400;
    line-height: 1;
    white-space: nowrap;
  }
  .card--front .school-box {
    left: 180px;
    top: 92px;
    width: 180px;
    height: 116px;
    font-size: 17px;
    letter-spacing: 0.5px;
  }

  /* Back: school name box, identity block, contact list, bottom rule */
  .card--back .school-box {
    left: 34px;
    top: 70px;
    width: 206px;
    height: 186px;
    font-size: 19px;
  }
  .identity {
    position: absolute;
    right: 34px;
    top: 26px;
    text-align: right;
  }
  .identity-name {
    font-family: "Cinzel", "Trajan Pro", Georgia, serif;
    font-size: 15px;
    font-weight: 600;
    letter-spacing: 0.3px;
  }
  .identity-role {
    font-size: 11px;
    margin-top: 3px;
  }
  .contact-list {
    position: absolute;
    right: 34px;
    top: 110px;
    list-style: none;
  }
  .contact-item {
    display: flex;
    align-items: center;
    justify-content: flex-end;
    gap: 10px;
    height: 21px;
    font-size: 11px;
  }
  .contact-icon {
    width: 14px;
    height: 14px;
    flex: none;
  }
  .rule-double {
    position: absolute;
    left: 0;
    right: 0;
    bottom: 30px;
    height: 5px;
    border-top: 1.5px solid var(--card-ink);
    border-bottom: 1.5px solid var(--card-ink);
  }
</style>
</head>
<body>
<main class="canvas">

  <section class="card card--front" aria-label="Business card front">
    <div class="frame-outer"></div>
    <div class="frame-inner"></div>
    <div class="school-box">Zottelgarten</div>
  </section>

  <section class="card card--back" aria-label="Business card back">
    <div class="school-box">Zottelgarten</div>

    <div class="identity">
      <p class="identity-name">Margit Wendler-Rasch</p>
      <p class="identity-role">Dipl. Dog Trainer</p>
    </div>

    <ul class="contact-list">
      <li class="contact-item">
        <span>Lindenweg 12, München</span>
        <svg class="contact-icon" viewBox="0 0 16 16" aria-hidden="true">
          <path d="M8 1.5 1 8h2v6.5h4v-4h2v4h4V8h2z" fill="#fff"/>
        </svg>
      </li>
      <li class="contact-item">
        <span>+49 89 2471190</span>
        <svg class="contact-icon" viewBox="0 0 16 16" aria-hidden="true">
          <path d="M3.5 1.5 6 4 4.8 5.8c.9 2.2 3.2 4.5 5.4 5.4L12 10l2.5 2.5-1.8 2C7.5 14.2 1.8 8.5 1.5 3.3z" fill="#fff"/>
        </svg>
      </li>
      <li class="contact-item">
        <span>info@zottelgarten.de</span>
        <svg class="contact-icon" viewBox="0 0 16 16" aria-hidden="true">
          <rect x="1" y="3.5" width="14" height="9" fill="#fff"/>
          <path d="M1 3.5 8 9l7-5.5" fill="none" stroke="#f78f20" stroke-width="1.2"/>
        </svg>
      </li>
      <li class="contact-item">
        <span>www.zottelgarten.de</span>
        <svg class="contact-icon" viewBox="0 0 16 16" aria-hidden="true">
          <g fill="none" stroke="#fff" stroke-width="1">
            <circle cx="8" cy="8" r="6.5"/>
            <ellipse cx="8" cy="8" rx="3" ry="6.5"/>
            <path d="M1.5 8h13M2.5 4.8h11M2.5 11.2h11"/>
          </g>
        </svg>
      </li>
    </ul>

    <div class="rule-double"></div>
  </section>

</main>
</body>
</html>
```